依頼詳細
【カラー】
・今のサイトのロゴやフォントに使用されているえんじ色は使用しなくて構いませ
ん。むしろ使用しないでください。
・薄いベージュや藍色をどこかに入れられたら入れてください。
必須ではないので入れなくても構いません。

【要素】
①グローバルナビ
・お知らせ
・ごあいさつ
・診療案内
・乳がん検診
・施設案内
・ご予約
・アクセスマップ
・よくある質問
・リンク

③トップコンテンツ
・お知らせ(ダミーテキストで構いません)
・ごあいさつ(ダミーテキストで構いません)
・診療案内(ダミーテキストで構いません)
┗診療時間/診療内容
診療内容の下層ページへ飛ぶリンク(ボタンなど)を貼ってください。
・乳がん検診(ダミーテキストで構いません)
乳がん検診の下層ページへ飛ぶリンク(ボタンなど)を貼ってください。
・施設案内(ダミーテキストで構いません)
施設案内の写真を表示
※のちに変更がありますが、とりあえず現状の施設の写真(下記URLより)を使って ください。
http://www.yurune-clinic.net/contents/shisetsu.htm
・アクセスマップ(ダミーテキストで構いません)
・よくある質問(ダミーテキストで構いません)
・リンク(ダミーテキストで構いません)
※使用する画像デザインはすべてお任せします。
※ご予約について
電話からのお問い合わせが多いので、スマホ利用時はそこから
電話ができる用にします。PC・スマホ共々、場所はご予約がしやすい所
でお願いします。お任せします。
サイトURL
http://www.yurune-clinic.net/
ページ数
2ページ
希望イメージ
• +5 0 +5
• シンプル
複雑
• 単色
カラフル
• 暗い
明るい
• 日常
高級
• 遊び心
厳粛
• 未来的
伝統的
• 女性的
男性的
希望する色
藍色、または薄いベージュ系の色を使用できそうなら使用してください。必ずではございません。
納品ファイル
• 高解像度JPG (.jpg)
• フォトショップ形式 (.psd)
補足説明
今回のコンペで当選された方には、中ページ(PC・スマホ)のデザイン制作を追加でお願いする可能性がございます。
報酬金額2万円程度を想定しておりますので、その際はお力添えお願いいたします。
依頼公開後の追記内容
現時点で、実質3案のご提案のみとなっており提案数に不安があるため、締め切り日を変更させていただきます。
現在いただいているご提案を拝見して、気になった点を下記にまとめておりますので今後ご提案いただける方はそちらもご留意いただけますと幸いです。
●あまり主張の強すぎる背景柄は避けたい
●ハイクオリティなイメージを喚起するため、極力すっきりとしたフォントが望ましい
(あまり丸みを帯びすぎていないもの等)
●フラットデザインのようなシンプルかつ洗練されたイメージが望ましい

ざっくりとした要望となってしまいますが、皆様のお力添えをいただければと思います。
引き続きよろしくお願いします。

病院系のサイトにはない新しいデザインと、小鳥という動物モチーフながら
動物病院のようにもならず、女性向けにきれいにまとまったデザインでした
pika-lune様のデザインを当選とさせていただきます。

この度は弊社デザインコンペへご提案いただき、誠にありがとうございました。
当選までに時間がかかり、皆様をお待たせしてしまいましたこと、お詫び申し上げます。
今回は、病院でありながら、病院らしくないサイトという無茶な依頼にも関わらず素敵なデザインが多く、とても参考になりました。
今後とも、弊社にお力添えいただけますと幸いです。
有難うございました。

```html
<!DOCTYPE html>
<html lang="ja">
<head>
<meta charset="utf-8">
<title>ゆるね乳腺・外科クリニック</title>
<link rel="stylesheet" href="https://fonts.googleapis.com/css2?family=Noto+Sans+JP:wght@400;500;700&family=Noto+Serif+JP:wght@400;600;700&display=swap">
<style>
:root{
  --navy:#2a2f6e;
  --navy-soft:#4a4f8c;
  --beige:#f6f2ea;
  --beige-line:#e6ddcc;
  --ink:#333;
  --muted:#777;
  --line:#d9d9d9;
  --white:#fff;
}
*{box-sizing:border-box;margin:0;padding:0}
html,body{width:1200px;height:4972px;overflow:hidden}
body{font-family:"Noto Sans JP",sans-serif;color:var(--ink);font-size:13px;line-height:1.8;background:var(--white);position:relative}
section{position:relative;width:1200px}
.sec-title{text-align:center}
.sec-title h2{font-family:"Noto Serif JP",serif;font-weight:600;font-size:22px;color:#222;letter-spacing:.1em}
.sec-title span{display:inline-block;margin-top:4px;background:var(--navy);color:#fff;font-size:9px;letter-spacing:.15em;padding:1px 22px;border-radius:2px}
.btn{display:block;width:180px;margin:0 auto;background:var(--navy);color:#fff;text-align:center;font-size:12px;padding:8px 0;border-radius:3px;text-decoration:none}
.btn::after{content:" ›"}
.ph{display:block}

/* hero */
.hero{height:380px;background:linear-gradient(180deg,#f1f1f3,#fafafa)}
.hero .ph{position:absolute;left:0;top:0;width:1030px;height:380px;background:linear-gradient(120deg,#e8e9ec 0%,#cfd2d8 40%,#9ea2ab 55%,#e3e4e7 75%,#f4f4f5 100%)}
.logo{position:absolute;left:345px;top:92px;display:flex;align-items:center;gap:14px;background:rgba(255,255,255,.85);padding:10px 20px}
.logo i{width:14px;height:14px;background:var(--navy);display:block}
.logo b{font-family:"Noto Serif JP",serif;font-weight:600;font-size:30px;color:var(--navy);display:block;line-height:1.2}
.logo small{font-family:"Noto Serif JP",serif;font-size:13px;color:var(--navy);letter-spacing:.08em;display:block}
.gnav{position:absolute;right:0;top:0;width:170px;background:#fff;border-left:1px solid var(--line)}
.gnav a{display:block;padding:10px 16px;font-size:11px;color:var(--ink);text-decoration:none;border-bottom:1px solid #eee}
.gnav a:first-child{background:var(--navy);color:#fff}

/* news */
.news{height:550px;padding-top:110px}
.news ul{list-style:none;width:620px;margin:30px auto 36px}
.news li{display:flex;gap:30px;font-size:12px;border-bottom:1px dotted var(--line);padding:10px 4px}
.news time{color:var(--muted)}

/* greeting */
.greet{height:360px;background:var(--beige);padding-top:30px;border-top:1px solid var(--beige-line)}
.greet .body{display:flex;width:940px;margin:26px auto 0;gap:40px}
.greet p{flex:1;font-size:11.5px;line-height:2}
.greet figure{width:300px;text-align:center}
.greet .ph{width:300px;height:200px;background:linear-gradient(160deg,#eef0f3,#c9ccd4)}
.greet figcaption{font-size:12px;margin-top:8px}

/* schedule */
.sched{height:600px;padding-top:36px}
.sched .cols{display:flex;gap:70px;width:960px;margin:28px auto 0}
.col{flex:1}
.col h3{text-align:center;font-size:15px;font-weight:600;border-bottom:2px solid var(--navy);padding-bottom:6px}
.col h4{text-align:center;font-size:12px;margin:12px 0 6px;font-weight:500}
table{width:100%;border-collapse:collapse;font-size:11px}
th,td{border:1px solid var(--line);text-align:center;padding:5px 0}
thead th{background:var(--navy);color:#fff;font-weight:400;line-height:1.4}
tbody th{background:#f2f2f5;width:60px;font-weight:400}
.dot{display:inline-block;width:10px;height:10px;border-radius:50%;background:var(--navy)}
.note{font-size:10px;color:var(--muted);margin:8px 0 14px;line-height:1.7}

/* screening */
.screen{height:400px}
.screen .ph{position:absolute;left:0;top:10px;width:480px;height:380px;background:radial-gradient(ellipse at 40% 50%,#f3c6d2 0%,#fbe9ee 40%,#fff 75%)}
.screen .sec-title{position:absolute;left:540px;top:20px;width:400px;text-align:center}
.screen .txt{position:absolute;left:540px;top:100px;width:400px;font-size:11.5px}
.screen .box{position:absolute;left:540px;top:160px;width:400px;border:2px solid var(--navy);padding:14px 18px;font-size:12px}
.screen .btn{position:absolute;left:650px;top:260px}

/* facility */
.facility{height:640px;padding-top:30px}
.grid{width:1000px;margin:24px auto 0;display:grid;grid-template-columns:repeat(3,1fr);gap:18px}
.grid figure{font-size:11px;text-align:center}
.grid .ph{height:200px}

/* access */
.access{height:690px;padding-top:30px}
.access .ph{width:720px;height:460px;margin:26px auto 0;background:linear-gradient(135deg,#ececec,#dcdcdc 50%,#e8e8e8)}
.access ul{list-style:none;width:720px;margin:20px auto 0;font-size:12px}
.access li{padding:3px 0 3px 16px;position:relative}
.access li::before{content:"";position:absolute;left:0;top:10px;width:8px;height:8px;background:var(--navy)}

/* faq */
.faq{height:530px;background:var(--beige);padding-top:30px}
.faq .items{width:880px;margin:24px auto 0}
.q{background:#fff;border:1px solid var(--beige-line);margin-bottom:14px}
.q h3{display:flex;align-items:center;gap:12px;font-size:13px;font-weight:500;padding:12px 16px}
.q h3 .mk{width:26px;height:26px;border-radius:50%;background:var(--navy);color:#fff;font-size:12px;display:flex;align-items:center;justify-content:center;font-family:"Noto Serif JP",serif}
.q h3 .ar{margin-left:auto;color:var(--navy)}
.q .a{display:flex;gap:12px;padding:12px 16px 14px;font-size:11.5px;border-top:1px dotted var(--line)}
.q .a .mk{flex:none;width:26px;height:26px;border-radius:50%;background:#b9a77f;color:#fff;font-size:12px;display:flex;align-items:center;justify-content:center}

/* links */
.links{height:420px;padding-top:30px}
.links .ph{position:absolute;left:0;top:0;width:300px;height:300px;background:radial-gradient(ellipse at 30% 40%,#c9dfb4 0%,#eaf3df 45%,rgba(255,255,255,0) 75%)}
.lgrid{position:relative;width:900px;margin:26px auto 0;display:grid;grid-template-columns:repeat(4,1fr);gap:12px}
.lgrid a{display:flex;justify-content:space-between;border:1px solid var(--line);padding:9px 12px;font-size:11px;color:var(--ink);text-decoration:none;background:#fff}
.lgrid a::after{content:"›";color:var(--navy)}

/* reserve */
.reserve{height:320px;padding-top:40px;text-align:center}
.reserve .frame{width:760px;margin:0 auto;border-top:1px solid var(--line);padding-top:22px}
.reserve h2{font-family:"Noto Serif JP",serif;font-weight:400;font-size:20px;letter-spacing:.15em}
.reserve .name{font-family:"Noto Serif JP",serif;font-weight:700;font-size:22px;margin-top:14px}
.tel{display:inline-flex;align-items:center;gap:12px;margin-top:14px;border:2px solid var(--navy);padding:8px 40px;font-size:34px;font-weight:700;color:var(--navy)}
.reserve p{font-size:11px;color:var(--muted);margin-top:14px}

footer{position:absolute;left:0;bottom:0;width:1200px;height:54px;background:var(--navy);color:#cfd1e6;font-size:10px;text-align:center;line-height:54px}
.pagetop{position:absolute;left:580px;bottom:54px;width:40px;height:20px;background:var(--navy);clip-path:polygon(0 100%,50% 0,100% 100%)}
</style>
</head>
<body>

<section class="hero">
  <div class="ph" role="img" aria-label="白い背景に置かれた聴診器の写真"></div>
  <div class="logo"><i></i><div><b>ゆるね乳腺・外科クリニック</b><small>Yurune Breast &amp; Surgery Clinic</small></div></div>
  <nav class="gnav">
    <a href="#">HOME</a><a href="#">お知らせ</a><a href="#">ごあいさつ</a><a href="#">診療案内</a><a href="#">乳がん検診</a><a href="#">施設案内</a><a href="#">ご予約</a><a href="#">アクセスマップ</a><a href="#">よくある質問</a><a href="#">リンク</a>
  </nav>
</section>

<section class="news">
  <div class="sec-title"><h2>お知らせ</h2><span>NEWS</span></div>
  <ul>
    <li><time>2016.00.00</time>ここに新着のお知らせのタイトルが入ります</li>
    <li><time>2016.00.00</time>ここに新着のお知らせのタイトルが入ります</li>
    <li><time>2016.00.00</time>ここに新着のお知らせのタイトルが入ります</li>
    <li><time>2016.00.00</time>ここに新着のお知らせのタイトルが入ります</li>
    <li><time>2016.00.00</time>ここに新着のお知らせのタイトルが入ります</li>
  </ul>
  <a class="btn" href="#">一覧はこちら</a>
</section>

<section class="greet">
  <div class="sec-title"><h2>ごあいさつ</h2><span>GREETING</span></div>
  <div class="body">
    <p>当院のご案内のために、まずはこちらをご覧ください。私たちは地域の皆さまが安心して受診できるよう、乳腺と外科の専門的な診療を丁寧に行っております。検査から治療、術後の経過観察まで、一人ひとりに寄り添った医療を心がけています。気になる症状がございましたら、どうぞお気軽にご相談ください。<br>ここには院長からのごあいさつ文が入ります。開院の想いや診療方針、スタッフ一同の取り組みなどを紹介する文章をここに掲載する予定です。今後とも地域に根ざしたクリニックとして努めてまいります。</p>
    <figure><div class="ph" role="img" aria-label="白衣姿の院長の写真"></div><figcaption>院長　結音 和彦</figcaption></figure>
  </div>
</section>

<section class="sched">
  <div class="sec-title"><h2>診療案内</h2><span>CONSULTATION</span></div>
  <div class="cols">
    <div class="col">
      <h3>乳腺・外科診療</h3><h4>診療時間</h4>
      <table>
        <thead><tr><th></th><th>午前<br>09:00〜12:30</th><th>午後<br>14:00〜18:00</th></tr></thead>
        <tbody>
          <tr><th>月</th><td><span class="dot"></span></td><td><span class="dot"></span></td></tr>
          <tr><th>火</th><td><span class="dot"></span></td><td><span class="dot"></span></td></tr>
          <tr><th>水</th><td><span class="dot"></span></td><td>手術</td></tr>
          <tr><th>木</th><td><span class="dot"></span></td><td><span class="dot"></span></td></tr>
          <tr><th>金</th><td><span class="dot"></span></td><td><span class="dot"></span></td></tr>
          <tr><th>土</th><td><span class="dot"></span></td><td>—</td></tr>
          <tr><th>日・祝</th><td>—</td><td>—</td></tr>
        </tbody>
      </table>
      <p class="note">※受付は診療終了の30分前までとなります<br>※休診：土曜午後、日曜、祝日</p>
      <a class="btn" href="#">診療内容はこちら</a>
    </div>
    <div class="col">
      <h3>リハビリテーション科・胃腸科</h3><h4>診療時間</h4>
      <table>
        <thead><tr><th></th><th>午前<br>09:00〜12:30</th><th>午後<br>14:00〜18:00</th></tr></thead>
        <tbody>
          <tr><th>月</th><td><span class="dot"></span></td><td><span class="dot"></span></td></tr>
          <tr><th>火</th><td><span class="dot"></span></td><td><span class="dot"></span></td></tr>
          <tr><th>水</th><td><span class="dot"></span></td><td><span class="dot"></span></td></tr>
          <tr><th>木</th><td><span class="dot"></span></td><td><span class="dot"></span></td></tr>
          <tr><th>金</th><td><span class="dot"></span></td><td><span class="dot"></span></td></tr>
          <tr><th>土</th><td><span class="dot"></span></td><td>—</td></tr>
          <tr><th>日・祝</th><td>—</td><td>—</td></tr>
        </tbody>
      </table>
      <p class="note">※受付は診療終了の30分前までとなります<br>※胃カメラは予約制です。詳しくはお問い合わせください</p>
      <a class="btn" href="#">診療内容はこちら</a>
    </div>
  </div>
</section>

<section class="screen">
  <div class="ph" role="img" aria-label="ピンクリボンのイメージ写真"></div>
  <div class="sec-title"><h2>乳がん検診</h2><span>SCREENING</span></div>
  <p class="txt">視触診・マンモグラフィ・超音波検査を組み合わせ、乳がんの早期発見に努めています。</p>
  <div class="box">当クリニックは、みなと市のマンモグラフィ検診の一次検診施設に認定されています。</div>
  <a class="btn" href="#">詳細はこちら</a>
</section>

<section class="facility">
  <div class="sec-title"><h2>施設案内</h2><span>FACILITY</span></div>
  <div class="grid">
    <figure><div class="ph" role="img" aria-label="待合ロビーの写真" style="background:linear-gradient(160deg,#dfe7ea,#a9bcc4)"></div>ロビー</figure>
    <figure><div class="ph" role="img" aria-label="診察室の写真" style="background:linear-gradient(160deg,#e6e3de,#b9b2a6)"></div>診察室・処置室</figure>
    <figure><div class="ph" role="img" aria-label="リハビリ室の写真" style="background:linear-gradient(160deg,#e4e6e8,#aeb3b8)"></div>リハビリテーション室</figure>
    <figure><div class="ph" role="img" aria-label="マンモグラフィ装置の写真" style="background:linear-gradient(160deg,#eeeeee,#b8bcc2)"></div>マンモグラフィ</figure>
    <figure><div class="ph" role="img" aria-label="超音波検査室の写真" style="background:linear-gradient(160deg,#e9e7ea,#b4b0b8)"></div>乳腺超音波（エコー）</figure>
    <figure><div class="ph" role="img" aria-label="クリニックの建物外観の写真" style="background:linear-gradient(180deg,#cfe0ef,#e7e3dc 50%,#bdb8ae)"></div>外観</figure>
  </div>
</section>

<section class="access">
  <div class="sec-title"><h2>アクセスマップ</h2><span>ACCESS</span></div>
  <div class="ph" role="img" aria-label="クリニック周辺の地図"></div>
  <ul>
    <li>みなと循環バス「みなと病院前」下車 徒歩3分</li>
    <li>みなと鉄道「みなと駅」より徒歩12分</li>
    <li>駐車場あり（15台）</li>
    <li>みなと市中央区〇〇町1-2-3（1階が受付です）</li>
  </ul>
</section>

<section class="faq">
  <div class="sec-title"><h2>Q&amp;A</h2><span>FAQ</span></div>
  <div class="items">
    <div class="q">
      <h3><span class="mk">Q</span>乳腺が張る・痛むのですが大丈夫ですか？<span class="ar">▲</span></h3>
      <div class="a"><span class="mk">A</span><p>乳腺の張りや痛みは、月経周期やホルモンの変化によって起こることが多く、多くの場合は心配いりません。ただし、しこりを触れる、分泌物がある、痛みが長く続くといった場合は、早めに受診して検査を受けることをおすすめします。ここに回答のダミーテキストが入ります。</p></div>
    </div>
    <div class="q"><h3><span class="mk">Q</span>乳がん検診ではどのような検査をしますか？<span class="ar">▼</span></h3></div>
    <div class="q"><h3><span class="mk">Q</span>予約なしでも受診できますか？待ち時間はどのくらいですか？<span class="ar">▼</span></h3></div>
  </div>
</section>

<section class="links">
  <div class="ph" role="img" aria-label="アイビーの葉のあしらい"></div>
  <div class="sec-title"><h2>リンク</h2><span>LINK</span></div>
  <div class="lgrid">
    <a href="#">乳腺臨床研究会</a><a href="#">乳がん検診推進協議会</a><a href="#">みなと市医師会</a><a href="#">外科医療ネット</a>
    <a href="#">地域がん相談窓口</a><a href="#">みなと市立病院</a><a href="#">女性の健康ナビ</a><a href="#">検診予約センター</a>
    <a href="#">医療情報ひろば</a><a href="#">リハビリ協会</a><a href="#">消化器医療会</a><a href="#">乳房ケア研究会</a>
    <a href="#">ピンクリボン広場</a><a href="#">みなと健康ガイド</a><a href="#">がん情報センター</a><a href="#">マンモ精度管理会</a>
  </div>
</section>

<section class="reserve">
  <div class="frame">
    <h2>ご予約はこちらから</h2>
    <div class="name">ゆるね乳腺・外科クリニック</div>
    <div class="tel"><svg width="30" height="30" viewBox="0 0 24 24" aria-hidden="true"><path fill="currentColor" d="M6.6 10.8a15.1 15.1 0 0 0 6.6 6.6l2.2-2.2c.3-.3.7-.4 1-.2 1.1.4 2.3.6 3.6.6.6 0 1 .4 1 1V20c0 .6-.4 1-1 1A17 17 0 0 1 3 4c0-.6.4-1 1-1h3.5c.6 0 1 .4 1 1 0 1.3.2 2.5.6 3.6.1.3 0 .7-.2 1z"/></svg>093-000-1234</div>
    <p>受付時間：平日 9:00〜18:00（土曜は12:30まで）<br>初めての方は保険証をお持ちのうえ、お電話にてご予約ください。</p>
  </div>
</section>

<div class="pagetop"></div>
<footer>Copyright © 2016 Yurune Breast &amp; Surgery Clinic. All Rights Reserved.</footer>
</body>
</html>
```